Plastering (solid plastering) business card design

We need a business card for a a small plastering business based in Perth Western Australia. We are a small team that provides a service in solid plastering specialising in float, white set and sand finish. We would like to see a clean business card with our name "Brightline Plastering" being the focus of the card and maybe incorporated into a logo. We don't have a logo at the moment so we would like to see some cards that may provide us with our future logo.

Industry/Entity Type

Business

Contact Information for Business Card

Brightline Plastering

Solid Plastering Specialists

Ph: Corey 0417683091
Ph: Liam 0468120357

Requirements
Should not have
• The design should not have Drywall incorporated into the card. In perth W.A. Plastering in different to someone that puts up Plyvane. We use sand, cement, lime and hardwall plaster.

```html
<!DOCTYPE html>
<html lang="en">
<head>
<meta charset="UTF-8">
<title>Brightline Plastering – Business Card</title>
<link href="https://fonts.googleapis.com/css2?family=Archivo+Black&family=Michroma&family=Arimo:wght@700&display=swap" rel="stylesheet">
<style>
  :root {
    --page-bg: #ffffff;
    --card-white: #ffffff;
    --card-fade: #e9e9e9;
    --ink: #111111;
    --orange-deep: #e8602a;
    --orange-light: #f4a623;
    --black-top: #2a2a2a;
    --black-bottom: #050505;
    --phone-white: #ffffff;
  }
  html, body {
    margin: 0;
    padding: 0;
    width: 1200px;
    height: 900px;
    overflow: hidden;
    background: var(--page-bg);
  }
  .canvas {
    position: relative;
    width: 1200px;
    height: 900px;
  }
  .card {
    position: absolute;
    left: 150px;
    top: 190px;
    width: 900px;
    height: 520px;
    border-radius: 34px;
    overflow: hidden;
    box-shadow: 0 18px 40px rgba(0,0,0,0.18);
    background: linear-gradient(180deg, var(--card-fade) 0%, var(--card-white) 45%);
  }
  .brand {
    position: absolute;
    left: 190px;
    top: 62px;
    display: flex;
    align-items: center;
    gap: 28px;
  }
  .brand-dot {
    width: 150px;
    height: 150px;
    border-radius: 50%;
    background: linear-gradient(180deg, var(--orange-light), var(--orange-deep));
    flex: none;
  }
  .brand-name {
    margin: 0;
    font-family: "Archivo Black", "Arial Black", sans-serif;
    font-weight: 400;
    font-size: 50px;
    line-height: 1.02;
    color: var(--ink);
    letter-spacing: 0.5px;
  }
  .tagline-band {
    position: absolute;
    left: 0;
    top: 300px;
    width: 100%;
    height: 44px;
    background: linear-gradient(90deg, var(--orange-deep) 0%, var(--orange-light) 50%, var(--orange-deep) 100%);
    display: flex;
    align-items: center;
    justify-content: center;
  }
  .tagline {
    margin: 0;
    font-family: "Michroma", "Arial", sans-serif;
    font-size: 15px;
    letter-spacing: 9px;
    color: var(--ink);
    text-transform: uppercase;
  }
  .contact-panel {
    position: absolute;
    left: 0;
    top: 344px;
    width: 100%;
    height: 176px;
    background: radial-gradient(ellipse at 50% 20%, var(--black-top) 0%, var(--black-bottom) 75%);
  }
  .contact-list {
    list-style: none;
    margin: 0;
    padding: 0;
    position: absolute;
    left: 290px;
    top: 26px;
  }
  .contact-item {
    display: flex;
    align-items: center;
    height: 46px;
    font-family: "Arimo", "Arial", sans-serif;
    font-weight: 700;
    font-size: 32px;
  }
  .phone-icon {
    width: 34px;
    height: 34px;
    margin-right: 12px;
    flex: none;
  }
  .contact-name {
    color: var(--orange-light);
    width: 120px;
  }
  .contact-number {
    color: var(--phone-white);
    letter-spacing: 1px;
  }
</style>
</head>
<body>
<div class="canvas">
  <div class="card">
    <div class="brand">
      <div class="brand-dot"></div>
      <h1 class="brand-name">Brightline<br>Plastering</h1>
    </div>

    <div class="tagline-band">
      <p class="tagline">Solid Plastering Specialists</p>
    </div>

    <div class="contact-panel">
      <ul class="contact-list">
        <li class="contact-item">
          <svg class="phone-icon" viewBox="0 0 34 34" aria-hidden="true">
            <circle cx="17" cy="17" r="15" fill="none" stroke="#f08a26" stroke-width="2.5"/>
            <path d="M11.5 9.5c1-.8 2-.6 2.6.3l1.6 2.5c.5.8.3 1.7-.4 2.2l-1 .7c.8 2 2.4 3.7 4.4 4.6l.8-1c.5-.7 1.5-.9 2.3-.4l2.4 1.6c.9.6 1 1.7.2 2.6l-1.2 1.3c-.9 1-2.4 1.2-3.8.6-4.5-1.9-7.9-5.4-9.6-9.9-.5-1.4-.2-2.8.8-3.7z" fill="#f08a26"/>
          </svg>
          <span class="contact-name">Corey</span>
          <span class="contact-number">:0417683091</span>
        </li>
        <li class="contact-item">
          <svg class="phone-icon" viewBox="0 0 34 34" aria-hidden="true">
            <circle cx="17" cy="17" r="15" fill="none" stroke="#f08a26" stroke-width="2.5"/>
            <path d="M11.5 9.5c1-.8 2-.6 2.6.3l1.6 2.5c.5.8.3 1.7-.4 2.2l-1 .7c.8 2 2.4 3.7 4.4 4.6l.8-1c.5-.7 1.5-.9 2.3-.4l2.4 1.6c.9.6 1 1.7.2 2.6l-1.2 1.3c-.9 1-2.4 1.2-3.8.6-4.5-1.9-7.9-5.4-9.6-9.9-.5-1.4-.2-2.8.8-3.7z" fill="#f08a26"/>
          </svg>
          <span class="contact-name">Liam</span>
          <span class="contact-number">:0468120357</span>
        </li>
      </ul>
    </div>
  </div>
</div>
</body>
</html>
```